Website Design for new Custom Homebuilder company R Pelbrook Homes

We need a website design for a new company based out of Liberty Hill, Texas called R Pelbrook Homes. We specialize in building unique, high end custom homes in Liberty Hill, Texas and the surrounding area. We would like to see designs that use the color black, white, copper and gold. Website needs to have a modern feel and the pages that have information about the company and then pages that have a gallery with pictures of completed homes and a page that has information on available homes.

```html
<!DOCTYPE html>
<html lang="en">
<head>
<meta charset="utf-8">
<title>R Pelbrook Homes — Custom Homes in Liberty Hill, Texas</title>
<link href="https://fonts.googleapis.com/css2?family=Open+Sans:ital,wght@0,400;0,600;0,700;1,400&family=Signika:wght@600;700&display=swap" rel="stylesheet">
<style>
:root{
  --copper:#8a5a2c;
  --band:#7b5432;
  --ink:#1d1d1d;
  --text:#333;
  --grey:#ebebec;
  --box:#e4e4e4;
  --white:#fff;
  --footer:#0e0e15;
}
*{box-sizing:border-box;margin:0;padding:0}
html,body{width:1200px;height:4399px;overflow:hidden}
body{position:relative;font-family:"Open Sans",sans-serif;color:var(--text);background:var(--white)}
.abs{position:absolute}

/* header */
.topbar{left:0;top:0;width:1200px;height:40px;background:var(--band);color:#f3e6d6;font-size:15px;z-index:3}
.topbar span{position:absolute;top:10px;display:flex;align-items:center;gap:6px}
.hero{left:0;top:0;width:1200px;height:642px;background:linear-gradient(180deg,#3b3c4e 0%,#6f6470 22%,#a88a76 38%,#5d5a52 55%,#3f4a2c 72%,#4f6a2a 100%)}
.nav{left:0;top:78px;width:1200px;height:30px;color:#fff;font-size:14px;z-index:3}
.nav a{position:absolute;color:#fff;text-decoration:none;top:6px;letter-spacing:.3px}
.nav-brand{left:470px;top:82px;width:260px;text-align:center;color:#fff;font-size:17px;font-weight:600;letter-spacing:1px;z-index:3}
.quote-btn{left:932px;top:67px;width:158px;height:52px;border:2px solid #fff;color:#fff;font-size:15px;font-weight:600;display:flex;align-items:center;justify-content:center;z-index:3}
.hero-brand{left:150px;top:405px;width:900px;text-align:center;color:#fff;font-size:60px;font-weight:600;letter-spacing:3px;line-height:1}
.hero-arrow{top:330px;width:50px;height:50px}

/* welcome */
.welcome{left:0;top:642px;width:1200px;height:300px;background:var(--grey);text-align:center}
.welcome h2{margin-top:65px;color:var(--copper);font-size:25px;font-weight:600}
.welcome p{width:985px;margin:26px auto 0;font-style:italic;font-size:17px;line-height:30px;color:#333}

/* about */
.eyebrow{font-weight:700;color:#111;font-size:19px;letter-spacing:.3px}
.title{color:var(--copper);font-family:"Signika",sans-serif;font-weight:700;font-size:36px;letter-spacing:.5px}
.about-text{left:111px;top:1090px;width:503px;font-size:15px;line-height:30px;text-align:justify;color:#222}
.btn-copper{background:var(--copper);color:#fff;font-size:16px;display:flex;align-items:center;justify-content:center;box-shadow:0 3px 6px rgba(0,0,0,.25)}

/* homes */
.homes{left:0;top:1516px;width:1200px;height:700px;background:var(--band)}
.card{top:1712px;width:302px;height:348px;background:#fff;box-shadow:0 3px 8px rgba(0,0,0,.3)}
.card .photo{height:188px;position:relative}
.card .tag{position:absolute;left:0;top:25px;background:var(--copper);color:#fff;font-size:13px;font-weight:600;padding:5px 15px}
.card .soon{position:absolute;left:0;right:0;top:85px;text-align:center;color:#fff;font-size:13px}
.card h3{font-size:15px;font-weight:700;color:#111;margin:18px 14px 0}
.card .sub{font-size:13px;margin:6px 14px 0;color:#222}
.card .specs{display:flex;gap:20px;margin:14px 14px 0;font-size:13px;color:#222}
.card .specs span{display:flex;align-items:center;gap:6px}
.card .price{position:absolute;left:0;right:0;bottom:0;height:40px;border-top:1px solid #ddd;display:flex;justify-content:space-between;align-items:center;padding:0 16px;font-size:15px;font-weight:700;color:#111}
.card .price b{color:var(--copper)}
.view-all{left:514px;top:2113px;width:172px;height:52px;border:2px solid #fff;color:#fff;font-size:16px;display:flex;align-items:center;justify-content:center}

/* services */
.center{left:0;width:1200px;text-align:center}
.service{top:2414px;height:374px;padding:34px 27px}
.service h3{font-size:19px;font-weight:700;color:#111}
.service hr{border:0;border-top:1px solid var(--copper);width:160px;margin:14px 0 26px}
.service p{font-size:15px;line-height:30px;text-align:justify;color:#333}
.service .more{display:flex;align-items:center;gap:10px;color:var(--copper);font-weight:600;font-size:15px;margin-top:10px}

/* gallery */
.tile{position:absolute}
.view-detail{color:#fff;font-size:17px;text-decoration:underline;display:flex;align-items:center;justify-content:center}

/* contact */
.contact{left:0;top:3488px;width:1200px;height:653px;background:var(--grey)}
.contact-item{left:111px;width:340px;height:60px;display:flex;gap:36px;font-size:15px;line-height:26px;color:#222}
.contact-icon{flex:none;width:54px;height:50px;background:var(--copper);display:flex;align-items:center;justify-content:center}
.field{background:#fff;color:#555;font-size:16px;padding:16px 20px}

/* footer */
.footer{left:0;top:4141px;width:1200px;height:258px;background:var(--footer);color:#fff;text-align:center}
.footer-brand{margin-top:72px;font-size:22px;font-weight:600;letter-spacing:1px}
.footer nav{margin-top:50px;display:flex;justify-content:center;gap:30px;font-size:16px;font-weight:600}
.footer p{margin-top:22px;font-size:15px}
</style>
</head>
<body>

<!-- header / hero -->
<div class="abs hero" role="img" aria-label="Photograph of a modern farmhouse-style stone home at dusk with a green lawn"></div>
<div class="abs topbar">
  <span style="left:110px">
    <svg width="14" height="14" viewBox="0 0 24 24" fill="none" stroke="#f3e6d6" stroke-width="2"><path d="M5 3h4l2 5-3 2a12 12 0 0 0 6 6l2-3 5 2v4a2 2 0 0 1-2 2A18 18 0 0 1 3 5a2 2 0 0 1 2-2z"/></svg>512.555.0147</span>
  <span style="left:266px">
    <svg width="13" height="13" viewBox="0 0 24 24" fill="none" stroke="#f3e6d6" stroke-width="2.5"><circle cx="10" cy="10" r="7"/><path d="M15 15l6 6"/></svg>search</span>
  <span style="right:110px">
    <svg width="16" height="13" viewBox="0 0 24 18" fill="none" stroke="#f3e6d6" stroke-width="2"><rect x="1" y="1" width="22" height="16"/><path d="M1 1l11 9 11-9"/></svg>hello@rpelbrookhomes.com</span>
</div>
<div class="abs nav">
  <svg class="abs" style="left:110px;top:8px" width="14" height="13" viewBox="0 0 24 22" fill="#fff"><path d="M12 1L1 11h3v10h6v-6h4v6h6V11h3z"/></svg>
  <a style="left:150px">ABOUT</a>
  <a style="left:224px">GALLERY</a>
  <a style="left:311px">AVAILABLE HOMES</a>
  <a style="left:770px">BLOG</a>
  <a style="left:833px">CONTACT</a>
</div>
<div class="abs nav-brand">R PELBROOK HOMES</div>
<div class="abs quote-btn">GET A QUOTE</div>

<div class="abs hero-brand">R PELBROOK HOMES</div>
<svg class="abs hero-arrow" style="left:30px" viewBox="0 0 50 50" fill="none" stroke="#ddd" stroke-width="2.5"><circle cx="25" cy="25" r="23"/><path d="M36 25H15M23 17l-8 8 8 8"/></svg>
<svg class="abs hero-arrow" style="left:1118px" viewBox="0 0 50 50" fill="none" stroke="#fff" stroke-width="3"><circle cx="25" cy="25" r="23"/><path d="M14 25h21M27 17l8 8-8 8"/></svg>
<svg class="abs" style="left:590px;top:588px" width="20" height="32" viewBox="0 0 20 32" fill="none" stroke="#fff" stroke-width="2.5"><path d="M10 2v27M2 21l8 8 8-8"/></svg>

<!-- welcome -->
<section class="abs welcome">
  <h2>WELCOME TO OUR COMPANY WEBSITE</h2>
  <p>Our MISSION, A dedicated pursuit and unwavering commitment to consistently exceed our client's expectations as we build luxury custom homes that we know will bring years of enjoyment, value and pride of ownership.&nbsp; At R Pelbrook Homes, building your dream is our MISSION</p>
</section>

<!-- about -->
<div class="abs eyebrow" style="left:111px;top:1002px">ABOUT</div>
<div class="abs title" style="left:111px;top:1030px">R PELBROOK HOMES</div>
<p class="abs about-text">R Pelbrook Homes understands that designing and building your dream home is the single most important investment you'll ever make.&nbsp; It can be one of life's most exciting and rewarding adventures, but it can also be overwhelming if your builder isn't committed to providing you with outstanding attention, communication and customer service.&nbsp; We are committed to making your homebuilding process an enjoyable experience. From the first handshake to the day that you unlock the door to your new home, we are there for you every step of the way. That's our promise and commitment to you.</p>
<div class="abs btn-copper" style="left:111px;top:1412px;width:137px;height:52px">LEARN MORE</div>
<div class="abs" role="img" aria-label="Portrait of the company founder standing in a bright finished kitchen" style="left:658px;top:1016px;width:430px;height:387px;background:linear-gradient(135deg,#dfe3e8,#c9c4bb 55%,#b08b62)"></div>

<!-- available homes -->
<section class="abs homes">
  <div class="abs center" style="top:68px;color:#111;font-weight:700;font-size:19px">LIBERTY HILL, TEXAS</div>
  <div class="abs center" style="top:96px;color:#fff;font-family:'Signika',sans-serif;font-weight:700;font-size:37px;letter-spacing:1px">AVAILABLE HOMES</div>
</section>

<article class="abs card" style="left:111px">
  <div class="photo" role="img" aria-label="Photograph of a stone home under a pink sunset sky" style="background:linear-gradient(180deg,#b76a7a,#d38f8a 35%,#8c8a84 60%,#5f7a3a)">
    <span class="tag">SOLD</span>
    <svg style="position:absolute;right:30px;bottom:-14px" width="34" height="34" viewBox="0 0 34 34"><circle cx="17" cy="17" r="17" fill="#8a5a2c"/><path d="M9 17h15M19 12l5 5-5 5" stroke="#fff" stroke-width="2.2" fill="none"/></svg>
  </div>
  <h3>114 CYPRESS RIDGE COVE</h3>
  <div class="sub" style="font-size:11px;font-weight:700">LIBERTY HILL, TEXAS</div>
  <div class="specs"><span><svg width="16" height="12" viewBox="0 0 16 12" fill="none" stroke="#333"><path d="M1 6h14v3H1zM3 9v2M13 9v2M3 6V2h3"/></svg>3 1/2 Bath</span><span><svg width="18" height="12" viewBox="0 0 18 12" fill="none" stroke="#333"><rect x="1" y="1" width="16" height="8"/><path d="M1 9v2M17 9v2M1 5h16"/></svg>4 Bed</span></div>
  <div class="price">Price:<b>$ 4,180,000</b></div>
</article>

<article class="abs card" style="left:449px">
  <div class="photo" role="img" aria-label="Photograph of a modern home at night, coming soon" style="background:linear-gradient(180deg,#2b2e38,#1d2029)">
    <span class="soon">COMING SOON</span>
  </div>
  <h3>LIBERTY HILL, TEXAS</h3>
  <div class="sub">Nemo enim ipsam voluptatem quiasam</div>
  <div class="specs"><span><svg width="16" height="12" viewBox="0 0 16 12" fill="none" stroke="#333"><path d="M1 6h14v3H1zM3 9v2M13 9v2M3 6V2h3"/></svg>3 Bath</span><span><svg width="18" height="12" viewBox="0 0 18 12" fill="none" stroke="#333"><rect x="1" y="1" width="16" height="8"/><path d="M1 9v2M17 9v2M1 5h16"/></svg>5 Bed</span></div>
  <div class="price">Price:<b>$ 4,180,000</b></div>
</article>

<article class="abs card" style="left:785px">
  <div class="photo" role="img" aria-label="Photograph of a modern home at night, coming soon" style="background:linear-gradient(180deg,#2b2e38,#1d2029)">
    <span class="tag" style="background:none">SOLD</span>
    <span class="soon">COMING SOON</span>
  </div>
  <h3>LIBERTY HILL, TEXAS</h3>
  <div class="sub">Nemo enim ipsam voluptatem quiasam</div>
  <div class="specs"><span><svg width="16" height="12" viewBox="0 0 16 12" fill="none" stroke="#333"><path d="M1 6h14v3H1zM3 9v2M13 9v2M3 6V2h3"/></svg>3 Bath</span><span><svg width="18" height="12" viewBox="0 0 18 12" fill="none" stroke="#333"><rect x="1" y="1" width="16" height="8"/><path d="M1 9v2M17 9v2M1 5h16"/></svg>5 Bed</span></div>
  <div class="price">Price:<b>$ 4,180,000</b></div>
</article>
<div class="abs view-all">VIEW ALL HOMES</div>

<!-- services -->
<div class="abs center eyebrow" style="top:2280px">SERVICES</div>
<div class="abs center title" style="top:2308px">WHAT WE OFFER</div>

<div class="abs service" style="left:111px;width:305px;background:var(--box)">
  <h3>Design.</h3><hr>
  <p>We can meet with you &amp; review your ideas, inspiration photos, or preliminary drawings and offermany suggestions on how to turn your concept into a reality.</p>
</div>
<div class="abs service" style="left:449px;width:304px;background:#fff;box-shadow:0 2px 10px rgba(0,0,0,.2)">
  <h3>House Placement.</h3><hr>
  <p>We can conduct a site visit at your land and offer suggestions for house placement.&nbsp; The positioning of a house on a piece of property has a major impact on the function of the home and property.</p>
  <div class="more">VIEW MORE <svg width="24" height="12" viewBox="0 0 24 12" fill="none" stroke="#8a5a2c" stroke-width="1.6"><path d="M0 6h22M17 1l5 5-5 5"/></svg></div>
</div>
<div class="abs service" style="left:784px;width:305px;background:var(--box)">
  <h3>Financing.</h3><hr>
  <p>We can refer you to a realtor for assistance locating the perfect home site based upon various factors including location, home site size, price point and school district.</p>
</div>

<!-- gallery -->
<div class="abs center eyebrow" style="top:2864px">GALLERY</div>
<div class="abs center title" style="top:2892px">OUR WORK</div>
<div class="tile" role="img" aria-label="Photograph of a covered patio with a stone fireplace" style="left:111px;top:2986px;width:261px;height:198px;background:linear-gradient(160deg,#4a4038,#9d8c74 50%,#2c2a28)"></div>
<div class="tile" role="img" aria-label="Photograph of a stone home exterior with a shaded lawn" style="left:111px;top:3200px;width:261px;height:200px;background:linear-gradient(180deg,#c6d3df,#8a8779 45%,#4f7a2c)"></div>
<div class="tile" role="img" aria-label="Photograph of a front porch with double glass doors and wreaths" style="left:391px;top:2986px;width:418px;height:414px;background:linear-gradient(180deg,#b7b1a4,#857b6b 40%,#2a2a2c 60%,#9aa2a8)"></div>
<div class="tile" role="img" aria-label="Photograph of a home courtyard with paver walkway" style="left:826px;top:2986px;width:263px;height:198px;background:linear-gradient(180deg,#b9cde3,#4a4d55 50%,#b3aa96)"></div>
<div class="tile view-detail" role="img" aria-label="Photograph of an open kitchen and living room with a chandelier" style="left:826px;top:3200px;width:263px;height:200px;background:linear-gradient(180deg,#a89c8c,#c9b9a4 60%,#8f7d68)">VIEW DETAIL</div>

<!-- contact -->
<section class="abs contact">
  <div class="abs center eyebrow" style="top:68px">CONTACT</div>
  <div class="abs center title" style="top:96px">GET IN TOUCH</div>
  <p class="abs center" style="top:168px;font-size:16px;line-height:30px;color:#222;padding:0 245px">Sed ut perspiciatis unde omnis iste natus error sit voluptatem accusantium doloremque laudantium, totam rem aperiam, eaque ipsa quae ab illo</p>
</section>

<div class="abs contact-item" style="top:3783px">
  <span class="contact-icon"><svg width="20" height="26" viewBox="0 0 20 26"><path d="M10 1a9 9 0 0 0-9 9c0 7 9 15 9 15s9-8 9-15a9 9 0 0 0-9-9z" fill="#fff"/><circle cx="10" cy="10" r="3.5" fill="#8a5a2c"/></svg></span>
  <div>318 Cedar Bluff Lane<br>Liberty Hill, Texas 78642</div>
</div>
<div class="abs contact-item" style="top:3862px">
  <span class="contact-icon"><svg width="22" height="22" viewBox="0 0 24 24" fill="#fff"><path d="M5 3h4l2 5-3 2a12 12 0 0 0 6 6l2-3 5 2v4a2 2 0 0 1-2 2A18 18 0 0 1 3 5a2 2 0 0 1 2-2z"/></svg></span>
  <div>CALL ON<br>512.555.0147</div>
</div>
<div class="abs contact-item" style="top:3937px">
  <span class="contact-icon"><svg width="24" height="17" viewBox="0 0 24 17"><rect width="24" height="17" fill="#fff"/><path d="M0 0l12 9 12-9" stroke="#8a5a2c" stroke-width="2" fill="none"/></svg></span>
  <div>MAIL AT<br>hello@rpelbrookhomes.com</div>
</div>
<div class="abs contact-item" style="top:4018px">
  <span class="contact-icon"><svg width="24" height="24" viewBox="0 0 24 24"><circle cx="12" cy="12" r="10" fill="none" stroke="#fff" stroke-width="2"/><path d="M2 12h20M12 2c-5 6-5 14 0 20M12 2c5 6 5 14 0 20" stroke="#fff" stroke-width="1.6" fill="none"/></svg></span>
  <div>VISIT US<br>www.rpelbrookhomes.com</div>
</div>

<div class="abs field" style="left:490px;top:3779px;width:293px;height:61px">First Name</div>
<div class="abs field" style="left:490px;top:3851px;width:293px;height:61px">Last Name</div>
<div class="abs field" style="left:490px;top:3923px;width:293px;height:61px">First Name</div>
<div class="abs field" style="left:490px;top:3995px;width:293px;height:61px">Last Name</div>
<div class="abs field" style="left:794px;top:3779px;width:293px;height:201px">Message</div>
<div class="abs btn-copper" style="left:794px;top:3995px;width:293px;height:61px;gap:14px;box-shadow:none">LAST NAME
  <svg width="18" height="16" viewBox="0 0 24 22" fill="#fff"><path d="M23 1L1 10l7 3 2 8 4-5 6 4z"/></svg></div>

<!-- footer -->
<footer class="abs footer">
  <div class="footer-brand">R PELBROOK HOMES</div>
  <nav><span>HOME</span><span>ABOUT</span><span>GALLERY</span><span>AVAILABLE HOUSE</span><span>BLOG</span><span>CONTACT</span></nav>
  <p>2022 R Pelbrook Homes. All Rights Reserved.</p>
</footer>

</body>
</html>
```